Erstellung eines Polizeiwimpels für Kinder
Zielgruppe
Wir stellen Fahrradwimpel für Kinder her. Hier finden Sie unsere Produkte: https://www.kramladen.de/stores/node/58203916472
Aufgabenstellung
Wir möchten einen 'Polizeiwimpel' für Kinder herstellen.
Wenn möglich, nur eine Farbe verwenden (reduziert Kosten in der Produktion). Der Hintergrund soll 'Polizei Blau' sein.
Wimpelgröße: 17,5 cm X 32 cm X 32cm (Dreieckig)
Ich habe ein selbst erstelltes Design hochgeladen. Es soll den Schriftzug 'Polizei' enthalten und evtl. noch 'Polizei Symbole', die Jungs (und ihre Eltern) ansprechen. (Pistole, Sheriffstern, etc.) Das offizielle Wappen oder andere Hoheitssymbole dürfen wir allerdings nicht verwenden.

```html
<!DOCTYPE html>
<html lang="de">
<head>
<meta charset="utf-8">
<title>Polizeiwimpel für Kinder</title>
<link rel="stylesheet" href="https://fonts.googleapis.com/css2?family=Arimo:wght@700&display=swap">
<style>
  :root {
    --police-blue: #025ca0;
    --ink-white: #ffffff;
    --page: #ffffff;
    --cut-line: #8a8a8a;
  }
  html, body {
    margin: 0;
    padding: 0;
    width: 780px;
    height: 1200px;
    overflow: hidden;
    background: var(--page);
  }
  .sheet {
    display: block;
    width: 780px;
    height: 1200px;
  }
  .pennant-shape { fill: var(--police-blue); }
  .dash { fill: var(--ink-white); }
  .pennant-title {
    font-family: "Arimo", Arial, Helvetica, sans-serif;
    font-weight: 700;
    fill: var(--ink-white);
  }
  .pennant-url {
    font-family: "Arimo", Arial, Helvetica, sans-serif;
    font-weight: 700;
    font-size: 14px;
    fill: var(--ink-white);
  }
  .cut-line {
    stroke: var(--cut-line);
    stroke-width: 1.2;
    stroke-dasharray: 1.5 1.5;
  }
</style>
</head>
<body>
<svg class="sheet" viewBox="0 0 1300 2000" xmlns="http://www.w3.org/2000/svg">

  <!-- Wimpel 1: schräge Variante -->
  <g class="pennant pennant--slanted">
    <polygon class="pennant-shape" points="123,213 1182,503 123,792"/>
    <g transform="translate(137,465) rotate(-15.3)">
      <g class="dash-row dash-row--top">
        <rect class="dash" x="0"   y="-10" width="58" height="20"/>
        <rect class="dash" x="91"  y="-10" width="58" height="20"/>
        <rect class="dash" x="182" y="-10" width="58" height="20"/>
        <rect class="dash" x="273" y="-10" width="58" height="20"/>
        <rect class="dash" x="364" y="-10" width="58" height="20"/>
      </g>
      <text class="pennant-title" x="14" y="177" font-size="133">POLIZEI</text>
      <g class="dash-row dash-row--bottom">
        <rect class="dash" x="-60" y="259" width="58" height="20"/>
        <rect class="dash" x="36"  y="259" width="58" height="20"/>
        <rect class="dash" x="132" y="259" width="58" height="20"/>
        <rect class="dash" x="228" y="259" width="58" height="20"/>
        <rect class="dash" x="324" y="259" width="58" height="20"/>
        <rect class="dash" x="420" y="259" width="58" height="20"/>
        <rect class="dash" x="516" y="259" width="58" height="20"/>
        <rect class="dash" x="612" y="259" width="58" height="20"/>
        <rect class="dash" x="708" y="259" width="58" height="20"/>
      </g>
    </g>
    <text class="pennant-url" transform="translate(961,530) rotate(-15.3)" textLength="131" lengthAdjust="spacingAndGlyphs">www.radwimpel.bike</text>
  </g>

  <line class="cut-line" x1="84" y1="993" x2="1205" y2="993"/>

  <!-- Wimpel 2: gerade Variante -->
  <g class="pennant pennant--straight">
    <polygon class="pennant-shape" points="123,1162 1183,1451 123,1741"/>
    <g class="dash-row dash-row--top">
      <rect class="dash" x="190" y="1356" width="56" height="20"/>
      <rect class="dash" x="282" y="1356" width="56" height="20"/>
      <rect class="dash" x="374" y="1356" width="56" height="20"/>
      <rect class="dash" x="465" y="1356" width="56" height="20"/>
      <rect class="dash" x="556" y="1356" width="56" height="20"/>
    </g>
    <text class="pennant-title" x="184" y="1497" font-size="107">POLIZEI</text>
    <g class="dash-row dash-row--bottom">
      <rect class="dash" x="190" y="1547" width="56" height="20"/>
      <rect class="dash" x="282" y="1547" width="56" height="20"/>
      <rect class="dash" x="374" y="1547" width="56" height="20"/>
      <rect class="dash" x="465" y="1547" width="56" height="20"/>
      <rect class="dash" x="556" y="1547" width="56" height="20"/>
    </g>
    <text class="pennant-url" transform="translate(193,1701) rotate(-15.3)" textLength="131" lengthAdjust="spacingAndGlyphs">www.radwimpel.bike</text>
  </g>

</svg>
</body>
</html>
```